A book about police officer shootings needs a dynamic cover design

I've almost completed a book on officer involved shootings...a very hot topic today. The title is "R.K.T. Beyond The Silence Fell." (emphasis on "beyond the silence") It details three separate shooting incidents, all within the same law enforcement family.I need a professional looking book cover that helps capture the drama. I attached a file of something I put together that is close, but I am concerned about "readability" and want a more professional look. I included a photo that I took off the internet of a gun being shot. That particular photo can stay or go, or be altered, but I like the perspective of the photo being fired from the person behind it. I wanted the cover to have the characteristics and color of a police uniform, utilizing blues, silvers, and maybe a little gold. I'm concerned about making sure the font and colors are also easy to read. I also will be working on a website design for "Beyond The Silence.Com" once the book hits the market. The back cover will incorporate the same colors, but only be a picture and excerpts from the book. I've included both for your review.

Target Market(s)

Law Enforcement, Christian, Media

Font styles to use
Sans Serif

Requirements
Must have
• A professional and readable appearance, that captures the drama of the topic. All the wording on the sample cover I attached, unless you come up with something better. A gun being fired from the perspective of the officer pulling the trigger. The size of the book will be the standard 6 x 9 in size. "Beyond The Silence" will eventually be my website domain and social media promotion hashtag.
Nice to have
• I would like the cover to incorporate the colors of a police uniform and badge, traditionally, navy blue, silver and some gold.
Should not have
• No police badge with a black band across. Not my topic.

```html
<!DOCTYPE html>
<html lang="en">
<head>
<meta charset="utf-8">
<title>R.K.T. Beyond The Silence Fell – Cover</title>
<link rel="stylesheet" href="https://fonts.googleapis.com/css2?family=Oswald:wght@300;400&family=Open+Sans:wdth,wght@75,300&family=PT+Sans&display=swap">
<style>
  :root{
    --navy:#0b1744;
    --deep:#0a1652;
    --royal:#2a48b8;
    --mist:#c9d4f0;
    --silver:#eef0f4;
    --silver-dark:#aab0bc;
    --gold:#e6cf7a;
    --gold-dark:#b8973e;
    --ink:#0c0c14;
    --white:#ffffff;
  }
  *{margin:0;padding:0;box-sizing:border-box}
  html,body{width:1200px;height:852px;overflow:hidden;background:var(--white)}
  .cover{position:relative;width:1200px;height:852px;overflow:hidden;font-family:"PT Sans",sans-serif}

  .light-condensed{font-family:"Open Sans",sans-serif;font-weight:300;font-stretch:75%}

  /* back */
  .back{position:absolute;left:0;top:0;width:568px;height:852px;
    background:radial-gradient(ellipse at 60% 55%,#4c6ad0 0%,var(--royal) 35%,#1c2f8c 70%,var(--deep) 100%)}
  .back-quote{position:absolute;right:24px;top:56px;width:500px;text-align:right;
    font-size:29px;line-height:40px;color:var(--white)}
  .portrait{position:absolute;width:120px;height:165px;background:linear-gradient(160deg,#5a6070,#1e222c)}
  .portrait.jim{left:37px;top:135px}
  .portrait.colin{left:413px;top:320px}
  .portrait.grant{left:37px;top:505px}
  .story{position:absolute;color:var(--white);font-size:15.5px;line-height:20px}
  .story .label{color:var(--mist);margin-bottom:1px}
  .story p.text{text-align:justify}
  .story.jim{left:180px;top:166px;width:368px}
  .story.colin{left:40px;top:342px;width:360px}
  .story.colin .label{text-align:right}
  .story.grant{left:180px;top:529px;width:368px}
  .isbn-box{position:absolute;left:358px;top:716px;width:167px;height:94px;background:var(--white)}
  .more-info{position:absolute;left:60px;top:742px;color:var(--white)}
  .more-info .small{font-size:17px}
  .more-info .url{font-size:24px;font-family:"PT Sans",sans-serif;font-weight:400;font-stretch:100%}

  /* spine */
  .spine{position:absolute;left:568px;top:0;width:64px;height:852px;background:linear-gradient(90deg,#050b2a,var(--navy) 50%,#050b2a)}
  .spine-text{position:absolute;left:9px;top:50px;height:752px;writing-mode:vertical-rl;
    font-family:"Oswald",sans-serif;font-weight:400;font-size:36px;letter-spacing:1px;color:var(--silver);white-space:nowrap;display:flex;justify-content:space-between}
  .spine-text .gold{color:var(--gold)}
  .spine-author{font-family:"PT Sans",sans-serif;font-size:34px;letter-spacing:0}

  /* front */
  .front{position:absolute;left:632px;top:0;width:568px;height:852px;
    background:radial-gradient(ellipse at 50% 72%,#b9c6f0 0%,#6f86d6 14%,#3450bc 38%,#1f3398 62%,var(--deep) 100%)}
  .front-quote{position:absolute;left:0;top:34px;width:568px;text-align:center;white-space:nowrap;
    font-family:"Oswald",sans-serif;font-weight:300;font-size:24px;line-height:32px;color:var(--ink)}
  .title{position:absolute;left:0;top:100px;width:568px;text-align:center;font-family:"Oswald",sans-serif;font-weight:400;line-height:1}
  .title .series{display:block;font-size:112px;
    background:linear-gradient(180deg,#f5e7a8,var(--gold) 50%,var(--gold-dark));-webkit-background-clip:text;background-clip:text;-webkit-text-fill-color:transparent;
    filter:drop-shadow(2px 3px 2px rgba(0,0,0,.45))}
  .title .main{display:block;font-size:104px;margin-top:6px;
    background:linear-gradient(180deg,var(--white),var(--silver) 55%,var(--silver-dark));-webkit-background-clip:text;background-clip:text;-webkit-text-fill-color:transparent;
    filter:drop-shadow(2px 3px 2px rgba(0,0,0,.5))}
  .author{position:absolute;left:0;top:458px;width:568px;text-align:center;font-family:"PT Sans",sans-serif;font-size:42px;line-height:54px;color:var(--ink)}
  .gun-scene{position:absolute;left:110px;top:528px;width:280px;height:324px;
    background:radial-gradient(ellipse at 50% 35%,#4a5a94 0%,#1a2256 55%,rgba(10,22,82,0) 80%)}
  .tagline{position:absolute;left:0;top:796px;width:568px;text-align:center;white-space:nowrap;
    font-family:"Oswald",sans-serif;font-weight:300;font-size:22px;line-height:30px;color:var(--ink)}
</style>
</head>
<body>
<div class="cover">
  <section class="back">
    <p class="back-quote light-condensed">“You cannot rely on anyone but yourself<br>to save your life…”</p>

    <div class="portrait jim" role="img" aria-label="Portrait photo of Lt. Dan Harlow in suit and tie"></div>
    <div class="story jim light-condensed">
      <p class="label">Lt. Dan Harlow’s Story:</p>
      <p class="text">“And then I heard it. The unmistakable sound of a shotgun being racked. And then another one. I was hit with near-blinding light from police flashlights, but was still able to make out the silhouettes of officers taking cover behind their patrol car doors… All weapons pointed directly at me…”</p>
    </div>

    <div class="story colin light-condensed">
      <p class="label">Colin Harlow’s Story:</p>
      <p class="text">“Colin stood over him, holding the shotgun in his left hand and his now empty handgun in his right. He stood there in stunned disbelief at how a routine call had escalated into a violent confrontation in a matter of seconds. The stench emanating from the house, mixed with the smell of gunpowder and blood, was almost overwhelming.”</p>
    </div>
    <div class="portrait colin" role="img" aria-label="Portrait photo of Colin Harlow in a dark polo shirt"></div>

    <div class="portrait grant" role="img" aria-label="Portrait photo of Officer Grant Harlow in uniform"></div>
    <div class="story grant light-condensed">
      <p class="label">Grant Harlow’s Story:</p>
      <p class="text">“Grant desperately wanted to stay with Nate, but the danger still presented by Kessler was paramount. As Grant rushed towards the suspended vehicle, the door suddenly opened. Kessler climbed out and dropped to the ground. He stood and faced Grant like a raging bull. If the bull charged, Grant was prepared to shoot again…”</p>
    </div>

    <div class="isbn-box"></div>
    <div class="more-info light-condensed">
      <p class="small">more info at</p>
      <p class="url">beyondthesilence.com</p>
    </div>
  </section>

  <section class="spine">
    <div class="spine-text">
      <span><span class="gold">R.K.T.</span>&nbsp; BEYOND THE SILENCE FELL</span>
      <span class="spine-author">Lt. Dan Harlow</span>
    </div>
  </section>

  <section class="front">
    <p class="front-quote">“IT WILL HAPPEN AND IT WILL COME OUT OF NOWHERE…”</p>
    <h1 class="title">
      <span class="series">R.K.T.</span>
      <span class="main">BEYOND THE<br>SILENCE FELL</span>
    </h1>
    <p class="author">Lt. Dan Harlow</p>
    <div class="gun-scene" role="img" aria-label="Photo from behind an officer firing a handgun, muzzle flash lighting the blue haze"></div>
    <p class="tagline">ONE LAW ENFORCEMENT FAMILY…THREE LIFE-CHANGING STORIES</p>
  </section>
</div>
</body>
</html>
```